"Letters From Fenwick Shoal" Fictional Book Cover

LETTERS FROM FENWICK SHOAL
By: Milo Verhaast

Here's the intro .

"It had been nearly forty years since Dale Oberfell last went to the island from where he was raised. Three months earlier he never would have thought about ever coming back. But life is weird. Things happen quickly and plans change, especially when your very life is at stake. The reason he was going back wasn’t to see old friends...no, no, no. They’re all dead. Of all the kids he grew up with on the island who moved off, he’s the only one still alive. Why?"

Pretty much all just a Lumora book, by the way.

Target Market(s)

fiction readers

Requirements
Must have
• Somewhat of a dark, mysterious cover is what I'd like to see. Use your imagination. I've never written a fiction book before so I'm very open to ideas

Needs to have my name, MILO VERHAAST at the bottom. like my other books, all of which are non-fiction
Nice to have
• Mysterious is what I'm looking for. NOT A HORROR story though. More a guy who left the island years ago, but is being called back to escape the rat race of modern, consumerist culture.

Please remember this NEEDS to jump out as a thumbnail on Brightcart as people are browsing. Mainly the WORDS need to stick out. Lighter words on a say a blue background.

If you want to try to use the attached pic, or something like this, to reflect an island in the cover, that'd be good.

I've also uploaded a couple images I purchased from Pixelvane, hopefully you can make something work with these.

```html
<!DOCTYPE html>
<html lang="en">
<head>
<meta charset="utf-8">
<title>Letters From Fenwick Shoal – Book Cover</title>
<link rel="stylesheet" href="https://fonts.googleapis.com/css2?family=Arvo:wght@700&family=Fira+Sans:wght@700&family=Josefin+Sans:wght@400&display=swap">
<style>
  :root {
    --page: #ffffff;
    --ink: #ffffff;
    --sky-top: #353f78;
    --sky-mid: #6a5a8e;
    --sky-glow: #e9856f;
    --sky-warm: #f0a07c;
    --sea: #4a3550;
    --sea-deep: #1c1626;
    --land: #07060a;
  }
  * { margin: 0; padding: 0; box-sizing: border-box; }
  html, body {
    width: 1200px; height: 856px; overflow: hidden;
    background: var(--page);
  }
  .canvas { position: relative; width: 1200px; height: 856px; }

  .wrap-art {
    position: absolute; left: 111px; top: 90px; width: 987px; height: 639px;
    background:
      radial-gradient(ellipse 380px 420px at 100% 100%, var(--land) 55%, rgba(7,6,10,0) 100%),
      radial-gradient(ellipse 300px 330px at 92% 62%, rgba(14,20,12,0.95) 40%, rgba(14,20,12,0) 100%),
      linear-gradient(180deg, rgba(0,0,0,0) 0%, rgba(0,0,0,0) 71%, var(--sea) 72%, var(--sea-deep) 100%),
      linear-gradient(180deg, var(--sky-top) 0%, var(--sky-mid) 30%, var(--sky-glow) 58%, var(--sky-warm) 68%, var(--sky-glow) 72%);
  }

  .title-big, .title-small, .front-title, .spine-title {
    font-family: "Arvo", Georgia, serif; font-weight: 700; color: var(--ink);
    text-transform: uppercase;
  }
  .author, .spine-author {
    font-family: "Fira Sans", Arial, sans-serif; font-weight: 700; color: var(--ink);
    text-transform: uppercase;
  }

  .back-cover { position: absolute; left: 111px; top: 90px; width: 480px; height: 639px; }
  .back-cover .title-big {
    position: absolute; left: 70px; top: 56px; white-space: nowrap;
    font-size: 62px; line-height: 1; letter-spacing: 2px;
  }
  .back-cover .title-small {
    position: absolute; left: 68px; top: 138px; white-space: nowrap;
    font-size: 24px; line-height: 1; letter-spacing: 1px;
  }
  .blurb {
    position: absolute; left: 68px; top: 204px; width: 340px;
    font-family: "Josefin Sans", Arial, sans-serif; font-size: 16px; line-height: 19px;
    font-variant: small-caps; letter-spacing: 0.4px; color: var(--ink);
  }
  .blurb p + p { margin-top: 19px; }
  .blurb .why { padding-left: 4px; }
  .back-cover .author {
    position: absolute; left: 68px; top: 530px; white-space: nowrap;
    font-size: 40px; line-height: 1; letter-spacing: 0.5px;
  }

  .spine-title, .spine-author {
    position: absolute; left: 605px; white-space: nowrap; line-height: 1;
    transform: translate(-50%, -50%) rotate(-90deg);
  }
  .spine-title { top: 510px; font-size: 17px; letter-spacing: 0.5px; }
  .spine-author { top: 240px; font-size: 20px; letter-spacing: 0.5px; }

  .front-cover { position: absolute; left: 640px; top: 90px; width: 458px; height: 639px; }
  .front-cover .author {
    position: absolute; left: 54px; top: 56px; white-space: nowrap;
    font-size: 40px; line-height: 1; letter-spacing: 0.5px;
  }
  .front-title {
    position: absolute; left: 0; width: 444px; top: 338px; text-align: center;
    font-size: 56px; line-height: 62px; letter-spacing: 1px;
  }
</style>
</head>
<body>
<div class="canvas">
  <div class="wrap-art" role="img" aria-label="Wraparound photograph of a coastal island at sunset: purple and orange sky over the sea on the back, a lighthouse on a wooded rocky cliff on the front"></div>

  <section class="back-cover">
    <div class="title-big">Letters</div>
    <div class="title-small">From Fenwick Shoal</div>
    <div class="blurb">
      <p>It had been nearly forty years since Dale Oberfell last went to the island from where he was raised. Three months earlier he never would have thought about ever coming back. But life is weird.</p>
      <p>Things happen quickly and plans change, especially when your very life is at stake. The reason he was going back wasn’t to see old friends...no, no, no. They’re all dead. Of all the kids he grew up with on the island who moved off, he’s the only one still alive.</p>
      <p class="why">Why?</p>
    </div>
    <div class="author">Milo Verhaast</div>
  </section>

  <div class="spine-title">Letters From Fenwick Shoal</div>
  <div class="spine-author">Milo Verhaast</div>

  <section class="front-cover">
    <div class="author">Milo Verhaast</div>
    <h1 class="front-title">Letters<br>From<br>Fenwick<br>Shoal</h1>
  </section>
</div>
</body>
</html>
```